Business Card Design

We need a business card design for a consulting firm which provides safety and risk management consulting services for public venues, hotels and tourist attractions. The business card design should include the attached logo unedited with a design based on incorporating the existing logo with a design of geometric patterns or lines on a predominantly white background.

Industry/Entity Type

Business

Contact Information for Business Card

Dane Morvello
Director & Principal Consultant

Ph: +61 (0) 468502 174
PO Box 456 Kellmore Vale, NSW Australia 2563
info@corvanwellandcare.com

(back of card to include website www.corvanwellandcare.com

```html
<!DOCTYPE html>
<html lang="en">
<head>
<meta charset="utf-8">
<title>Corvan Welland Care – Business Card</title>
<link rel="stylesheet" href="https://fonts.googleapis.com/css2?family=Lato:wght@400;700;900&display=swap">
<style>
  :root {
    --brand-blue: #1f8fc9;
    --brand-blue-deep: #1a7db3;
    --brand-green: #6cbb3c;
    --ink: #222222;
    --muted: #6b6b6b;
    --paper: #ffffff;
    --backdrop: #e9ebee;
  }
  * { margin: 0; padding: 0; box-sizing: border-box; }
  html, body { width: 1200px; height: 926px; overflow: hidden; }
  body {
    background: var(--backdrop);
    font-family: "Lato", Arial, sans-serif;
    position: relative;
  }
  .card {
    position: absolute;
    left: 250px;
    width: 700px;
    height: 400px;
    background: var(--paper);
    overflow: hidden;
    box-shadow: 0 4px 14px rgba(0,0,0,0.12);
  }
  .card--front { top: 42px; }
  .card--back { top: 484px; }
  .card__art { position: absolute; inset: 0; width: 100%; height: 100%; }

  .brand {
    position: absolute;
    display: flex;
    align-items: center;
    gap: 12px;
  }
  .brand__dot {
    width: 18px; height: 18px;
    border-radius: 50%;
    background: var(--brand-green);
  }
  .brand__name {
    font-weight: 900;
    color: var(--brand-blue);
    letter-spacing: 0.5px;
    text-transform: uppercase;
    white-space: nowrap;
  }
  .card--front .brand { top: 52px; right: 40px; }
  .card--front .brand__name { font-size: 28px; }

  .person {
    position: absolute;
    top: 192px;
    right: 40px;
    text-align: right;
  }
  .person__name {
    font-size: 27px;
    font-weight: 900;
    color: var(--brand-blue);
    text-transform: uppercase;
    letter-spacing: 0.5px;
  }
  .person__role {
    font-size: 17px;
    font-weight: 700;
    color: var(--ink);
    margin-top: 2px;
  }

  .contact {
    position: absolute;
    left: 34px;
    top: 134px;
    list-style: none;
    color: var(--paper);
    font-size: 16px;
  }
  .contact__item {
    display: flex;
    align-items: center;
    gap: 8px;
    margin-bottom: 10px;
  }
  .contact__icon { width: 14px; height: 14px; flex: none; }

  .address {
    position: absolute;
    left: 34px;
    bottom: 34px;
    color: var(--paper);
    font-size: 19px;
    letter-spacing: 1.6px;
    text-transform: uppercase;
  }

  .card--back .brand {
    top: 150px;
    left: 0; right: 0;
    justify-content: center;
  }
  .card--back .brand__name { font-size: 34px; }
  .website {
    position: absolute;
    top: 218px;
    left: 0; right: 0;
    text-align: center;
    font-size: 16px;
    font-weight: 700;
    letter-spacing: 3px;
    color: var(--muted);
  }
</style>
</head>
<body>

  <section class="card card--front" aria-label="Business card front">
    <svg class="card__art" viewBox="0 0 700 400" preserveAspectRatio="none" aria-hidden="true">
      <rect width="700" height="400" fill="var(--brand-blue)"/>
      <path d="M105,0 C240,15 280,178 385,246 C470,300 600,306 700,296" fill="none" stroke="var(--paper)" stroke-width="5"/>
      <path d="M300,296 C440,345 590,330 700,292 L700,322 C590,360 440,360 300,296 Z" fill="var(--brand-green)"/>
      <path d="M130,0 C260,10 300,160 400,230 C480,285 600,290 700,280 L700,0 Z" fill="var(--paper)"/>
    </svg>

    <div class="brand">
      <span class="brand__dot"></span>
      <span class="brand__name">Corvan Welland Care</span>
    </div>

    <div class="person">
      <p class="person__name">Dane Morvello</p>
      <p class="person__role">Director &amp; Principal Consultant</p>
    </div>

    <ul class="contact">
      <li class="contact__item">
        <svg class="contact__icon" viewBox="0 0 16 16" aria-hidden="true"><path fill="currentColor" d="M3.6 1.2l2.3 2.6-1.3 1.8c.9 2 2.3 3.5 4.4 4.5l1.7-1.3 2.7 2.2-1 2.6C7 14 2 9 1.2 3.1z"/></svg>
        <span>+61 (0) 468502 174</span>
      </li>
      <li class="contact__item">
        <svg class="contact__icon" viewBox="0 0 16 16" aria-hidden="true"><rect x="1" y="3" width="14" height="10" fill="currentColor"/><path d="M1 3l7 6 7-6" fill="none" stroke="var(--brand-blue)" stroke-width="1.4"/></svg>
        <span>info@corvanwellandcare.com</span>
      </li>
    </ul>

    <p class="address">PO Box 456 Kellmore Vale, NSW Australia 2563</p>
  </section>

  <section class="card card--back" aria-label="Business card back">
    <svg class="card__art" viewBox="0 0 700 400" preserveAspectRatio="none" aria-hidden="true">
      <path d="M600,0 L700,0 L700,60 Z" fill="var(--brand-blue)"/>
    </svg>
    <div class="brand">
      <span class="brand__dot"></span>
      <span class="brand__name">Corvan Welland Care</span>
    </div>
    <p class="website">www.corvanwellandcare.com</p>
  </section>

</body>
</html>
```